Pharmacy Moving Flyer Design

We are a community pharmacy that is relocating to new premises and as a result changing our name also. Our current name is Bramble Lane Pharmacy and our new name will be Red Kite Pharmacy. I want to include a relocation map and also stress the fact that the only thing changing is the name and the location. Everything else will stay the same but newer!
Current address is 47 Maple Row, Oswestry, SY11 4LN. New address Red Kite Pharmacy, 82 Foxley Parade, Oswestry, SY11 5DT. The phone numbers will remain the same - 01691 738425 and 0800 4538062. The date for opening in our new location is Monday 17th November 2014.

Industry/Entity Type

Pharmacy

```html
<!DOCTYPE html>
<html lang="en">
<head>
<meta charset="utf-8">
<title>Red Kite Pharmacy – Moving Flyer</title>
<link rel="stylesheet" href="https://fonts.googleapis.com/css2?family=Oswald:wght@500;600&family=Roboto+Condensed:wght@400;500;700&family=Arimo:wght@700&display=swap">
<style>
  :root {
    --stage: #e9e6e2;
    --purple: #8e3f9c;
    --purple-band: #c3a6cd;
    --purple-soft: #d9c6df;
    --purple-deep: #5b3f66;
    --panel: #f4eff6;
    --ink: #1b1b1b;
    --ink-soft: #333;
    --red: #c8191f;
    --frame: #464646;
    --map: #e6e3dc;
    --pin-grey: #6d6d6d;
  }
  * { box-sizing: border-box; margin: 0; padding: 0; }
  html, body { width: 1200px; height: 1000px; overflow: hidden; }
  body { background: var(--stage); position: relative; font-family: "Roboto Condensed", Arial, sans-serif; color: var(--ink); }

  .flyer { position: absolute; width: 640px; overflow: hidden; box-shadow: 0 2px 8px rgba(0,0,0,.25); }
  .flyer--front { left: 55px; top: 28px; height: 450px; background: var(--purple-soft); }
  .flyer--back { left: 500px; top: 510px; height: 445px; }

  /* front */
  .hero-photo { position: absolute; left: 0; top: 0; width: 640px; height: 258px;
    background: linear-gradient(135deg, #e8dced 0%, #d6c4de 45%, #c9b2d3 75%, #b99cc6 100%); }
  .truck-art { position: absolute; left: 35px; top: 12px; width: 568px; height: 238px;
    background: linear-gradient(90deg, #4d4d4d 0%, #5a4a60 55%, #8e3f9c 72%, #8e3f9c 100%);
    border-radius: 4px 40px 18px 4px; opacity: .9; }
  .sign { position: absolute; left: 35px; top: 12px; width: 352px; height: 178px; background: #fff;
    border: 6px solid var(--frame); text-align: center; padding-top: 10px; }
  .sign__old-name { font-family: "Arimo", Arial, sans-serif; font-size: 18px; color: var(--ink); }
  .sign__old-address { font-size: 11px; letter-spacing: 1.5px; color: #444; margin-top: 1px; }
  .sign__headline { font-family: "Arimo", Arial, sans-serif; font-size: 29px; line-height: 32px; color: var(--red); margin-top: 10px; }

  .open-band { position: absolute; left: 0; top: 256px; width: 640px; height: 62px; background: var(--purple-band); text-align: center; }
  .open-band__date { font-family: "Oswald", sans-serif; font-weight: 600; font-size: 22px; color: #fff; line-height: 30px; padding-top: 4px; }
  .open-band__label { font-size: 13px; letter-spacing: 10px; color: var(--purple-deep); font-weight: 700; margin-top: 1px; }

  .address-panel { position: absolute; left: 8px; top: 318px; width: 624px; height: 122px; background: var(--panel); }
  .brand { position: absolute; display: flex; align-items: center; gap: 12px; }
  .brand__mark { width: 58px; height: 58px; border-radius: 50%; background: var(--purple); flex: none; }
  .brand__name { font-size: 31px; line-height: 30px; font-weight: 500; color: var(--ink); letter-spacing: 1px; }
  .address-panel .brand { left: 17px; top: 14px; }
  .address-panel__address { position: absolute; left: 17px; top: 84px; font-size: 18px; letter-spacing: .3px; font-weight: 500; }
  .map-pin { position: absolute; left: 330px; top: 6px; }
  .phones { position: absolute; left: 432px; top: 18px; font-size: 17px; line-height: 19px; font-weight: 500; }
  .phones__number { font-size: 22px; font-weight: 700; line-height: 24px; }

  /* back */
  .back-photo { position: absolute; inset: 0; background: linear-gradient(160deg, #d3b9dc 0%, #c4a2cf 50%, #b48dc2 100%); }
  .map-area { position: absolute; left: 20px; top: 10px; width: 382px; height: 278px; background: var(--map); border: 4px solid #fff; }
  .opening { position: absolute; left: 430px; top: 24px; width: 200px; text-align: center; font-family: "Oswald", sans-serif;
    font-weight: 600; font-size: 23px; line-height: 28px; color: #fff; }
  .opening sup { font-size: 12px; }
  .callout { position: absolute; left: 293px; top: 130px; width: 285px; height: 142px; background: #fff; box-shadow: 0 1px 4px rgba(0,0,0,.3); }
  .callout .brand { left: 18px; top: 14px; gap: 10px; }
  .callout .brand__mark { width: 48px; height: 48px; }
  .callout .brand__name { font-size: 25px; line-height: 24px; }
  .callout__address { position: absolute; left: 78px; top: 66px; font-size: 19px; line-height: 24px; font-weight: 500; }
  .callout__tel { position: absolute; left: 78px; top: 118px; font-size: 11px; font-weight: 500; }
  .services { position: absolute; left: 8px; top: 318px; width: 620px; height: 75px; background: rgba(255,255,255,.55);
    display: flex; gap: 40px; padding: 11px 0 0 26px; font-size: 14.5px; line-height: 17px; color: var(--ink-soft); }
  .services p { width: 262px; }
  .services p + p { width: 290px; }
  .welcome { position: absolute; left: 8px; top: 396px; width: 620px; height: 40px; background: rgba(255,255,255,.35);
    text-align: center; font-size: 21px; font-weight: 500; line-height: 40px; color: var(--ink-soft); }
</style>
</head>
<body>

<section class="flyer flyer--front">
  <div class="hero-photo" role="img" aria-label="Purple-toned photo of tablets and capsules"></div>
  <div class="truck-art" role="img" aria-label="Illustration of a removal truck with a dark grey body and purple cab"></div>
  <div class="sign">
    <p class="sign__old-name">BRAMBLE LANE PHARMACY</p>
    <p class="sign__old-address">47 MAPLE ROW, OSWESTRY</p>
    <h1 class="sign__headline">WE ARE MOVING<br>AND CHANGING<br>OUR NAME !</h1>
  </div>

  <div class="open-band">
    <p class="open-band__date">WE WILL OPEN IN OUR NEW HOME ON NOVEMBER 17TH 2014</p>
    <p class="open-band__label">OUR NEW ADDRESS IS</p>
  </div>

  <div class="address-panel">
    <div class="brand">
      <span class="brand__mark"></span>
      <span class="brand__name">RED KITE<br>PHARMACY</span>
    </div>
    <p class="address-panel__address">82 FOXLEY PARADE, OSWESTRY, SY11 5DT</p>

    <svg class="map-pin" width="70" height="110" viewBox="0 0 70 110" aria-label="See the map on the back">
      <path d="M35 2 C16 2 2 16 2 35 C2 56 24 70 32 96 L38 96 C46 70 68 56 68 35 C68 16 54 2 35 2 Z" fill="var(--pin-grey)"/>
      <circle cx="35" cy="35" r="27" fill="#fff"/>
      <ellipse cx="35" cy="104" rx="8" ry="3" fill="#999"/>
      <g font-family="Roboto Condensed, sans-serif" font-weight="700" font-size="9" fill="#222" text-anchor="middle">
        <text x="35" y="25">SEE</text>
        <text x="35" y="35">THE MAP</text>
        <text x="35" y="45">ON THE</text>
        <text x="35" y="55">BACK</text>
      </g>
    </svg>

    <div class="phones">
      <p>OUR PHONE NUMBERS<br>REMAIN THE SAME:</p>
      <p class="phones__number">01691 738425<br>0800 4538062</p>
    </div>
  </div>
</section>

<section class="flyer flyer--back">
  <div class="back-photo" role="img" aria-label="Soft purple photo of tablets and capsules"></div>
  <div class="map-area" role="img" aria-label="Street map showing the new pharmacy location"></div>

  <p class="opening">OPENING ON<br>MONDAY<br>17<sup>TH</sup> NOV. 2014</p>

  <div class="callout">
    <div class="brand">
      <span class="brand__mark"></span>
      <span class="brand__name">RED KITE<br>PHARMACY</span>
    </div>
    <p class="callout__address">82 FOXLEY PARADE,<br>OSWESTRY, SY11 5DT</p>
    <p class="callout__tel">TEL: 01691 738425 &nbsp;|&nbsp; 0800 4538062</p>
  </div>

  <div class="services">
    <p>We offer a full repeat prescription<br>management service tailored to suit you,<br>including free home delivery if required.</p>
    <p>Our other services include Blood Pressure<br>Monitoring, New Medicine Service,<br>Medicines Review and Compliance Packs.</p>
  </div>
  <p class="welcome">We look forward to welcoming you to Red Kite Pharmacy.</p>
</section>

</body>
</html>
```